Healthy Products Company Needs to Refresh Their Web Image

This is a web relaunch for a company that creates a nutritional supplement made out of Greenlipped Mussels that are native to and grow only in New Zealand. This product is a health superfood which is excellent support for many conditions such as arthritis, heart disease, joint mobility, and healthy lung function, etc. Trevolin Marine is a pioneer in this industry having started in 1967. They have pioneered and are the only company in the business to use cool drying methodology to dry their mussels. This low heat process doesn't degrade nutritional and health giving properties of the mussels. The final design should communicate, cool, healthy, green and natural feeling superimposed on cutting edge technology, and pharmaceutical purity. Natural yet scientific. Also a certain solidity and trustworthiness.
Updates

Hi: The web site name is www.trevolin.com and I would like to have both the psd file and the underlying code.
Thank you.

Target Market(s)

Corporates: Pharmaceutical Companies, Heath Product Companies

Industry/Entity Type

Pharmaceutical

Requirements
Must have
• Currently we have no way to order the product online and we will not be doing this in the current site. However, capability to do that in the future would be nice.
Please see the previous web site for understanding of what the company does. Plese feel free to run with any ideas you may have in layout or content. I have enclosed a new logo for the company. Please make sure you carry the style of the logo throughout the new web site. I don't have any new pictures we can use right now but I will include a background picture you can use for now as a placeholder.

```html
<!DOCTYPE html>
<html lang="en">
<head>
<meta charset="utf-8">
<title>Trevolin Marine</title>
<link rel="stylesheet" href="https://fonts.googleapis.com/css2?family=Figtree:wght@400;500;600&family=Open+Sans:wght@400;600&display=swap">
<style>
:root{
  --blue:#3a8fe0;
  --blue-light:#6cb4f5;
  --blue-dark:#1f6fc7;
  --link:#1a78d8;
  --heading:#2f6aa5;
  --green:#4caf4f;
  --green-dark:#1e8a3a;
  --panel:#f9f9f9;
  --body-text:#9a9a9a;
  --card-text:#b0b0b0;
  --ink:#222;
  --sky:#a9d4ee;
}
*{margin:0;padding:0;box-sizing:border-box}
html,body{width:1200px;height:1067px;overflow:hidden}
body{position:relative;font-family:"Figtree",sans-serif;color:var(--ink);
  background:linear-gradient(180deg,#fff 0,#fff 260px,#dcedf8 560px,var(--sky) 1067px)}
.brand{position:absolute;left:127px;top:38px;display:flex;align-items:center;gap:12px}
.brand-dot{width:46px;height:46px;border-radius:50%;background:var(--green-dark)}
.brand-name{font-size:34px;font-weight:500;color:var(--green-dark)}
.contact{position:absolute;left:841px;top:48px}
.contact-phone{font-size:19px;font-weight:500;color:#111}
.contact-mail{font-size:14px;margin-top:6px}
.contact-mail a{color:var(--link);text-decoration:none;border-bottom:1px solid #9cc6ef}
.main-nav{position:absolute;left:110px;top:123px;width:980px;height:47px;display:flex;
  border-radius:6px 6px 0 0;border:1px solid var(--blue-dark);border-bottom:none;
  background:linear-gradient(180deg,#5eaaf0,var(--blue) 55%,#2f82d8)}
.main-nav a{display:flex;align-items:center;justify-content:center;color:#fff;text-decoration:none;
  font-size:13.5px;font-weight:600;text-shadow:0 1px 1px rgba(0,0,0,.3);border-right:1px solid #2a78cc;
  box-shadow:inset -1px 0 0 #6cb7f6}
.main-nav a:last-child{border-right:none;box-shadow:none}
.panel{position:absolute;left:89px;top:170px;width:1022px;height:816px;background:var(--panel);
  border-top:7px solid var(--blue-light);border-bottom:5px solid var(--blue-light);border-radius:8px}
.hero{position:absolute;left:110px;top:198px;width:979px;height:300px;border-radius:6px;overflow:hidden}
.hero-photo{position:absolute;inset:0;background:linear-gradient(90deg,#5a4a2a 0,#b87a2a 35%,#7a6a4a 55%,#e9e4de 75%,#f2eee8 100%)}
.hero-title{position:absolute;left:47px;top:92px;font-family:"Open Sans",sans-serif;font-weight:600;
  font-size:45px;line-height:42px;letter-spacing:-1.6px;color:#fff;text-shadow:0 1px 3px rgba(0,0,0,.35)}
.card{position:absolute;top:519px;width:316px;height:186px;background:#fff;border:1px solid #ddd;border-radius:3px;overflow:hidden}
.card-head{height:43px;background:linear-gradient(180deg,#5cbf5a,var(--green) 50%,#2f9a3f);
  color:#fff;font-size:16px;font-weight:600;padding:11px 18px;border-bottom:1px solid var(--green-dark)}
.card-photo{position:absolute;left:0;top:50px;width:142px;height:130px;border-radius:40%}
.card-text{position:absolute;left:154px;top:53px;width:148px;height:100px;overflow:hidden;
  font-family:"Open Sans",sans-serif;font-size:11.5px;line-height:16.7px;color:var(--card-text)}
.card-more{position:absolute;left:156px;top:160px;font-size:13px;color:var(--link);text-decoration:none;border-bottom:1px solid #9cc6ef}
.welcome-title{position:absolute;left:107px;top:741px;font-size:25px;font-weight:400;letter-spacing:-.6px;color:var(--heading)}
.welcome-body{position:absolute;left:110px;top:782px;width:750px;font-family:"Open Sans",sans-serif;font-size:14.3px;line-height:23px;color:var(--body-text)}
.welcome-body p{margin-bottom:9px}
.welcome-photo{position:absolute;left:878px;top:767px;width:211px;height:158px;border-radius:4px;
  background:linear-gradient(180deg,#6d9ccc 0,#9cbfe0 45%,#c9b48e 70%,#e0c640 100%)}
.foot-nav a{position:absolute;top:1007px;font-size:12.5px;color:#333;text-decoration:none}
.copyright{position:absolute;top:1033px;left:0;width:1170px;text-align:center;font-size:12px;color:#333}
</style>
</head>
<body>
<header>
  <div class="brand"><span class="brand-dot"></span><span class="brand-name">Trevolin Marine</span></div>
  <div class="contact">
    <div class="contact-phone">CALL NOW: +64 3 555 0142</div>
    <div class="contact-mail">Email: <a href="#">sales@trevolin.com</a></div>
  </div>
  <nav class="main-nav">
    <a href="#" style="width:99px">HOME</a>
    <a href="#" style="width:171px">THE TREVOLIN STORY</a>
    <a href="#" style="width:222px">PRODUCT SPECIFICATIONS</a>
    <a href="#" style="width:241px">BACKGROUND INFORMATION</a>
    <a href="#" style="width:133px">CONTACT US</a>
    <a href="#" style="flex:1">SITE MAP</a>
  </nav>
</header>

<div class="panel"></div>

<section class="hero">
  <div class="hero-photo" role="img" aria-label="Green-lipped mussels with a smiling older couple"></div>
  <h1 class="hero-title">Produces a fresh powder<br>of natural foods for the<br>Health Foods.</h1>
</section>

<article class="card" style="left:110px">
  <div class="card-head">Mucopolysaccharides</div>
  <div class="card-photo" role="img" aria-label="Green-lipped mussel shells" style="background:radial-gradient(ellipse at 50% 55%,#4f8f80,#2e5d55 60%,transparent 72%)"></div>
  <p class="card-text">A key factor in human metabolism, growth and health is a group of com-plex carbohydrates called mucopolysaccharides, (MPS). MPS are long chain</p>
  <a class="card-more" href="#">Read more</a>
</article>
<article class="card" style="left:442px">
  <div class="card-head">Bioactive Nutrition from Nature</div>
  <div class="card-photo" role="img" aria-label="Closed dark mussels" style="background:radial-gradient(ellipse at 50% 55%,#3a3a3a,#111 60%,transparent 72%)"></div>
  <p class="card-text">A key factor in human metabolism, growth and health is a group of com-plex carbohydrates called mucopolysaccharides, (MPS). MPS are long chain</p>
  <a class="card-more" href="#">Read more</a>
</article>
<article class="card" style="left:773px">
  <div class="card-head">The Cradle of Life</div>
  <div class="card-photo" role="img" aria-label="Open mussel with orange flesh" style="background:radial-gradient(ellipse at 50% 55%,#e8a22a,#2a2a2a 58%,transparent 72%)"></div>
  <p class="card-text">A key factor in human metabolism, growth and health is a group of com-plex carbohydrates called mucopolysaccharides, (MPS). MPS are long chain</p>
  <a class="card-more" href="#">Read more</a>
</article>

<section>
  <h2 class="welcome-title">Welcome to Greenleaf Clinic Health&nbsp; Suplements</h2>
  <div class="welcome-body">
    <p>Lorem Ipsum est simplement du faux texte employé dans la sition et la misen page avant impression. Le Lorem Ipsum est le faux texte standard de l'imprimerie depuis les années 1500, quand un peintre anonyme assembla ensemble.</p>
    <p>Morceaux de texte pour réaliser un livre spécimen de polices de texte. Il n'a pas fait que survivre cinq siècles, mais s'est aussi adapté à la bureautique informatique, sans que son contenu n'en soit modifié. Il a été popularisé dans les années 1960.</p>
  </div>
  <div class="welcome-photo" role="img" aria-label="Older couple smiling by the sea"></div>
</section>

<footer>
  <nav class="foot-nav">
    <a href="#" style="left:132px">HOME</a>
    <a href="#" style="left:210px">THE TREVOLIN STORY</a>
    <a href="#" style="left:357px">PRODUCT SPECIFICATIONS</a>
    <a href="#" style="left:549px">BACKGROUND INFORMATION</a>
    <a href="#" style="left:752px">CONTACT US</a>
    <a href="#" style="left:863px">SITE MAP</a>
  </nav>
  <p class="copyright">© Copyright Hivewell Australia 2011</p>
</footer>
</body>
</html>
```